Grand Opening Post Card

We need a post card for a new fitness and yoga studio located in Reading, MA. We provide one on one training, small group training, fitness classes, yoga, youth training, nutritional guidance and prenatal fitness. The final design should introduce our company to the community and encourage them to attend our Grand Opening.
Grand Opening Date: Saturday, September 13, 2014 10-2pm
Face Painting, balloons, door prizes, drinks and snacks, fitness demos, Yoga demos, meet and greet the Personal Trainers and Yoga Instructors. 212 Alder Lane, Reading, MA 01892 781-555-0374
www.vantoro-studio.example
Tag Line: Strengthen, Stretch, Succeed
We want to add that the font for our logo is Serpentine LT Medium
Our colors are Red, Black, Gray, and White
Our studio is contemporary
Designs are close to the mark so far. I apologize for not responding sooner, but I have not been able to log on to my account since Sunday. Thanks!
I added to the project description and added a couple of photos.
Residents of Reading
Fitness

```html
<!DOCTYPE html>
<html lang="en">
<head>
<meta charset="utf-8">
<title>Vantoro Studio – Grand Opening</title>
<link rel="stylesheet" href="https://fonts.googleapis.com/css2?family=Arimo:wght@400;700&family=Jura:wght@500&family=Mr+Dafoe&display=swap">
<style>
  :root {
    --red-glow: #d8303c;
    --red-mid: #b01c27;
    --red-deep: #6a0a10;
    --white: #ffffff;
    --ink: #111111;
    --photo-floor: #5d5a5c;
    --photo-wall: #cfcac4;
    --photo-team: #2a2a2c;
    --photo-team-wall: #d9d9db;
    --script-shadow: rgba(60, 0, 6, 0.6);
  }
  * { margin: 0; padding: 0; box-sizing: border-box; }
  html, body { width: 900px; height: 1200px; overflow: hidden; }
  body { background: #7a7a7a; }

  .postcard {
    position: relative;
    width: 900px;
    height: 1200px;
    overflow: hidden;
    background: radial-gradient(ellipse 72% 62% at 29% 52%, var(--red-glow) 0%, var(--red-mid) 50%, var(--red-deep) 100%);
    color: var(--white);
  }

  .photo {
    position: absolute;
    z-index: 1;
    background: var(--white);
    padding: 10px;
    box-shadow: 3px 5px 12px rgba(0, 0, 0, 0.45);
  }
  .photo__fill { width: 100%; height: 100%; }
  .photo--studio { left: 368px; top: 66px; width: 414px; height: 326px; transform: rotate(-1deg); }
  .photo--studio .photo__fill {
    background: linear-gradient(180deg, var(--photo-wall) 0%, var(--photo-wall) 30%, var(--photo-floor) 55%, #3e3c3e 100%);
  }
  .photo--team { left: 478px; top: 814px; width: 366px; height: 282px; transform: rotate(-4deg); }
  .photo--team .photo__fill {
    background: linear-gradient(180deg, var(--photo-team-wall) 0%, var(--photo-team-wall) 28%, var(--photo-team) 58%, #1a1a1c 100%);
  }

  .highlights {
    position: absolute;
    right: 540px;
    top: 206px;
    font-family: "Jura", sans-serif;
    font-weight: 500;
    font-size: 21px;
    line-height: 37px;
    text-align: right;
    white-space: nowrap;
  }

  .studio-name {
    position: absolute;
    left: 388px;
    top: 410px;
    font-family: "Arimo", sans-serif;
    font-weight: 700;
    font-size: 60px;
    line-height: 62px;
    color: var(--ink);
  }

  .event-details {
    position: absolute;
    left: 439px;
    top: 552px;
    font-family: "Arimo", sans-serif;
    font-size: 22px;
    line-height: 28px;
    list-style: none;
    white-space: nowrap;
  }
  .event-details__item { padding-bottom: 4px; }
  .event-details__item--ruled { border-bottom: 1.5px solid rgba(255, 255, 255, 0.85); margin-bottom: 9px; }
  .event-details__item--date { width: 234px; }
  .event-details__item--time { width: 292px; }

  .headline {
    position: absolute;
    inset: 0;
    z-index: 2;
    pointer-events: none;
  }
  .headline__svg { width: 900px; height: 1200px; display: block; }
  .headline__line {
    font-family: "Mr Dafoe", cursive;
    font-size: 118px;
    fill: var(--white);
    filter: drop-shadow(5px 6px 0 var(--script-shadow));
  }
</style>
</head>
<body>
  <main class="postcard">
    <figure class="photo photo--studio">
      <div class="photo__fill" role="img" aria-label="Photo of the studio training floor with weight racks, dumbbells and medicine balls"></div>
    </figure>

    <p class="highlights">face painting,<br>balloons, door prizes,<br>drinks and snacks,<br>fitness demos, yoga<br>demos, meet and<br>greet the personal<br>trainers and yoga<br>instructors.</p>

    <h2 class="studio-name">Vantoro<br>Studio</h2>

    <ul class="event-details">
      <li class="event-details__item event-details__item--ruled event-details__item--date">Saturday, September 13</li>
      <li class="event-details__item event-details__item--ruled event-details__item--time">10am to 2pm</li>
      <li class="event-details__item">212 Alder Lane, Reading, MA</li>
      <li class="event-details__item">Call: 01892 781-555-0374</li>
    </ul>

    <figure class="photo photo--team">
      <div class="photo__fill" role="img" aria-label="Group photo of the studio's personal trainers and yoga instructors in black shirts"></div>
    </figure>

    <h1 class="headline">
      <svg class="headline__svg" viewBox="0 0 900 1200" aria-label="Grand Opening">
        <text class="headline__line" x="96" y="850" transform="rotate(-16 96 850)">Grand</text>
        <text class="headline__line" x="200" y="984" transform="rotate(-16 200 984)">Opening</text>
      </svg>
    </h1>
  </main>
</body>
</html>
```